Corvallin Property Solutions need a business card design

Hello guys. We would need a business card design asap please.
We are a start up property investment business based in London UK specialised in buying, selling, managing and letting properties and helping distressed property owners.
The name of our Business is Corvallin, the logo symbolises the four fundamental elements of the world (earth, air, fire and water) and so it stands for strength, stability, longevity.
We would like the business card to communicate professionalism and reliability. Many many thanks indeed for your work.

Details:

1.) Marisol Dunkley
Property Investor
Mobile: +44(0)7700362517
Email: marisol.corvallin@quilbrook.example

2.) Tomas Brindle
Property Investor
Mobile: +44(0)7700845926
Email: tomas.corvallin@quilbrook.example

Industry/Entity Type

Investment

```html
<!DOCTYPE html>
<html lang="en">
<head>
<meta charset="utf-8">
<title>Corvallin Property Solutions – Business Card</title>
<link rel="stylesheet" href="https://fonts.googleapis.com/css2?family=Josefin+Sans:wght@300;400;600;700&display=swap">
<style>
  :root {
    --stage: #2e2f31;
    --ink: #141414;
    --red: #d7373c;
    --green: #3aa547;
    --blue: #3f66b4;
    --card-front-top: #d9464a;
    --card-front-mid: #e7d9d9;
    --card-front-low: #4aa35a;
    --card-front-end: #4771b8;
    --card-back-light: #f6f5f4;
    --card-back-shade: #d6d4d2;
  }
  * { box-sizing: border-box; margin: 0; padding: 0; }
  html, body {
    width: 1200px;
    height: 800px;
    overflow: hidden;
    background: var(--stage);
    font-family: "Josefin Sans", sans-serif;
    color: var(--ink);
  }
  .stage {
    position: relative;
    width: 1200px;
    height: 800px;
  }
  .card {
    position: absolute;
    top: 140px;
    width: 330px;
    height: 520px;
    overflow: hidden;
  }
  .card-front { left: 225px; }
  .card-back  { left: 645px; }

  .card-front .backdrop {
    position: absolute;
    inset: 0;
    background: linear-gradient(180deg,
      var(--card-front-top) 0%,
      var(--card-front-mid) 38%,
      var(--card-front-low) 65%,
      var(--card-front-end) 100%);
  }
  .card-back .backdrop {
    position: absolute;
    inset: 0;
    background: linear-gradient(150deg, var(--card-back-light) 0%, #ebeae8 55%, var(--card-back-shade) 100%);
  }

  .front-brand {
    position: absolute;
    left: 0;
    right: 0;
    top: 285px;
    text-align: center;
  }
  .front-brand .wordmark {
    font-weight: 700;
    font-size: 37px;
    letter-spacing: 1.5px;
    color: var(--ink);
  }
  .front-brand .tagline {
    margin-top: 10px;
    font-weight: 600;
    font-size: 16px;
    letter-spacing: 1.2px;
    color: var(--ink);
  }

  .back-content {
    position: absolute;
    left: 70px;
    top: 150px;
    right: 20px;
  }
  .back-brand .wordmark {
    font-weight: 700;
    font-size: 22px;
    letter-spacing: 1px;
  }
  .back-brand .tagline {
    margin-top: 3px;
    font-weight: 600;
    font-size: 9px;
    letter-spacing: 0.8px;
  }
  .person {
    margin-top: 42px;
  }
  .person .name {
    font-weight: 600;
    font-size: 20px;
    letter-spacing: 0.5px;
  }
  .person .role {
    margin-top: 2px;
    font-weight: 400;
    font-size: 13px;
    color: var(--red);
  }
  .contact {
    margin-top: 18px;
  }
  .contact .label {
    font-weight: 400;
    font-size: 11px;
    letter-spacing: 0.5px;
  }
  .contact .label.mobile { color: var(--green); }
  .contact .label.email  { color: var(--blue); }
  .contact .value {
    font-weight: 300;
    font-size: 18px;
  }
  .contact .value.email-address {
    font-size: 13.5px;
    font-weight: 400;
  }
</style>
</head>
<body>
<main class="stage">

  <section class="card card-front" aria-label="Business card front">
    <div class="backdrop" role="img" aria-label="Soft red, green and blue faceted background"></div>
    <div class="front-brand">
      <div class="wordmark">CORVALLIN</div>
      <div class="tagline">PROPERTY SOLUTIONS</div>
    </div>
  </section>

  <section class="card card-back" aria-label="Business card back">
    <div class="backdrop" role="img" aria-label="Light grey faceted background"></div>
    <div class="back-content">
      <div class="back-brand">
        <div class="wordmark">CORVALLIN</div>
        <div class="tagline">PROPERTY SOLUTIONS</div>
      </div>
      <div class="person">
        <div class="name">TOMAS BRINDLE</div>
        <div class="role">Property Investor</div>
      </div>
      <div class="contact">
        <div class="label mobile">MOBILE</div>
        <div class="value">+44(0)7700845926</div>
      </div>
      <div class="contact">
        <div class="label email">EMAIL</div>
        <div class="value email-address">tomas.corvallin@quilbrook.example</div>
      </div>
    </div>
  </section>

</main>
</body>
</html>
```